Yoga Studio Postcard Advertising Flyer

Need a postcard size flyer that will promote our business. The objective is to promote location and availability. Want it to be personal. The objective to connect the audience to the purpose of yoga and the focus on enabling functional well-being. Something that is a very big focus at this point in time in the world. I really want people to see the value in connecting with us via our website, calmora app, pagewell or vibro. The colours are to be bright but not overwhelming and aligned to the logo colours. Its also important to have the location picture on the flyer - unless you think that it is way too much (try a with or without). I don't want this to be a specials brochure - it is an introduction to our brand and our business. No need to over do it with promotional lines apart from come and join us.

Delayed in organising this.

Local yogis and residence who are or want to be focused on well-being.

• Pictures - would have the logo on one side.
• Modern and aligned to website design.

```html
<!DOCTYPE html>
<html lang="en">
<head>
<meta charset="utf-8">
<title>Willow Crane Yoga – Flyer</title>
<link rel="stylesheet" href="https://fonts.googleapis.com/css2?family=Comfortaa:wght@700&family=Rubik:wght@800&family=Caveat:wght@500&family=Catamaran:wght@700&family=Montserrat:wght@600&family=Roboto:wght@700&display=swap">
<style>
  :root {
    --bg-top: #c9e4bb;
    --bg-mid: #f4f9f2;
    --bg-low: #d6eacb;
    --teal: #14b396;
    --teal-soft: #7fd6c1;
    --sky: #29aae2;
    --forest: #3a5a1f;
    --navy: #1d2f5c;
    --ink: #4a4a4a;
    --headline: #6b6b6b;
    --white: #ffffff;
  }
  * { box-sizing: border-box; margin: 0; padding: 0; }
  html, body { width: 855px; height: 1200px; overflow: hidden; background: #fff; }
  .flyer {
    position: relative;
    width: 855px; height: 1200px; overflow: hidden;
    background: linear-gradient(180deg, var(--bg-top) 0%, #e6f2df 40%, var(--bg-mid) 62%, var(--bg-low) 100%);
  }
  .waves { position: absolute; inset: 0; width: 855px; height: 1200px; }
  .venue-photo {
    position: absolute; left: 142px; top: -8px; width: 584px; height: 584px;
    border-radius: 50%; border: 6px solid var(--white);
    background: linear-gradient(180deg, #8fb4dd 0%, #cfd9e3 35%, #c9c6c0 60%, #9b7b66 85%, #5d6b45 100%);
    box-shadow: 0 2px 8px rgba(0,0,0,.12);
  }
  .headline {
    position: absolute; left: 44px; top: 52px;
    font-family: "Comfortaa", sans-serif; font-weight: 700; font-style: italic;
    font-size: 49px; line-height: 63px; color: var(--headline);
    -webkit-text-stroke: 1.5px var(--white); paint-order: stroke fill;
    text-shadow: 0 0 3px #fff, 1px 1px 0 #fff, -1px -1px 0 #fff;
  }
  .brand {
    position: absolute; left: 662px; top: 34px; width: 180px; text-align: center;
    font-family: "Montserrat", sans-serif; font-weight: 600; color: var(--navy);
  }
  .brand-dot { width: 58px; height: 58px; border-radius: 50%; background: var(--sky); margin: 0 auto 22px; }
  .brand-name { font-size: 21px; line-height: 26px; letter-spacing: .5px; }
  .join-card {
    position: absolute; left: 216px; top: 527px; width: 430px; height: 173px;
    border: 2px solid #d9d9d9; background: transparent;
  }
  .join-card-inner {
    position: absolute; left: 14px; top: 12px; width: 400px; height: 150px;
    background: var(--white); box-shadow: 2px 3px 4px rgba(0,0,0,.25);
    text-align: center;
  }
  .join-title {
    font-family: "Rubik", sans-serif; font-weight: 800; font-size: 41px;
    color: var(--forest); margin-top: 12px; line-height: 48px; letter-spacing: .5px;
  }
  .join-url { font-family: "Caveat", cursive; font-size: 30px; color: var(--navy); line-height: 34px; }
  .join-social {
    display: flex; justify-content: center; align-items: center; gap: 14px; margin-top: 12px;
    font-family: "Caveat", cursive; font-size: 22px; color: var(--forest);
  }
  .join-social .channel { color: var(--navy); }
  .studio-photo {
    position: absolute; left: 17px; top: 745px; width: 254px; height: 283px;
    background: linear-gradient(180deg, #f1efeb 0%, #e4e0da 45%, #2f4f7a 62%, #a0522d 78%, #5a2e17 100%);
  }
  .values { position: absolute; left: 278px; top: 742px; width: 560px; }
  .values h2 {
    font-family: "Catamaran", sans-serif; font-weight: 700; font-size: 38px;
    color: var(--forest); line-height: 44px; margin-bottom: 6px;
  }
  .values p {
    font-family: "Montserrat", sans-serif; font-weight: 600; font-size: 17px;
    color: var(--ink); letter-spacing: 1px; line-height: 28px; margin-bottom: 11px;
  }
  .phone-band { position: absolute; left: 0; top: 1039px; width: 440px; height: 70px; }
  .phone {
    position: absolute; left: 70px; top: 1052px; display: flex; align-items: center; gap: 10px;
    font-family: "Roboto", sans-serif; font-weight: 700; font-size: 35px; color: var(--white);
  }
  .footer {
    position: absolute; left: 0; top: 1106px; width: 855px; height: 94px; background: var(--sky);
    text-align: center; color: var(--white);
    font-family: "Roboto", sans-serif; font-weight: 700; font-size: 19px;
    padding-top: 17px; line-height: 28px;
  }
  .footer .address { display: inline-flex; align-items: center; gap: 12px; }
</style>
</head>
<body>
<main class="flyer">
  <svg class="waves" viewBox="0 0 855 1200" aria-hidden="true">
    <path d="M0 370 C120 360 190 470 240 560 C260 600 220 620 205 560 C170 460 90 420 0 420 Z" fill="var(--teal-soft)" opacity=".55"/>
    <path d="M0 395 C130 395 190 480 225 560 C160 470 80 440 0 445 Z" fill="var(--teal)" opacity=".6"/>
    <path d="M640 560 C720 470 780 300 855 240 L855 300 C800 340 760 470 690 560 C660 600 630 610 640 560 Z" fill="var(--teal-soft)" opacity=".5"/>
    <path d="M620 600 C700 560 790 560 855 520 L855 590 C780 610 700 610 620 600 Z" fill="var(--teal)" opacity=".35"/>
  </svg>

  <div class="venue-photo" role="img" aria-label="Photo of the white chapel building that houses the studio, under a blue sky"></div>

  <h1 class="headline">Enable<br>Functional<br>Wellbeing!!!</h1>

  <div class="brand">
    <div class="brand-dot"></div>
    <div class="brand-name">WILLOW CRANE<br>YOGA</div>
  </div>

  <section class="join-card">
    <div class="join-card-inner">
      <div class="join-title">COME JOIN US!</div>
      <div class="join-url">www.willowcraneyoga.com.au</div>
      <div class="join-social">
        <span>Find us on</span>
        <span class="channel">calmora</span>
        <span class="channel">pagewell</span>
        <span class="channel">vibro</span>
      </div>
    </div>
  </section>

  <div class="studio-photo" role="img" aria-label="Photo of the studio interior with yoga mats and blocks on a timber floor in warm sunlight"></div>

  <section class="values">
    <h2>Our Value</h2>
    <p>Strengthen your well-being through adaptive yoga.</p>
    <p>Seek to evolve your mind and body through the challenge of yoga.</p>
    <p>Perfection is a desire and never an outcome through the practice of yoga.</p>
    <p>Our vision is to create an atmosphere that enables inclusiveness of the whole community.</p>
  </section>

  <svg class="phone-band" viewBox="0 0 440 70" aria-hidden="true">
    <path d="M0 0 H330 C380 0 410 30 435 70 H0 Z" fill="var(--teal)"/>
  </svg>
  <div class="phone">
    <svg width="26" height="30" viewBox="0 0 24 28" aria-hidden="true">
      <path d="M6 2 C4 2 2 5 2 9 C3 17 9 25 17 27 C20 27 22 25 22 23 L18 19 C17 18 15 19 14 21 C10 19 7 14 7 10 C9 9 10 8 10 6 Z" fill="none" stroke="var(--white)" stroke-width="2.4" stroke-linejoin="round"/>
    </svg>
    <span>0400 316 842</span>
  </div>

  <footer class="footer">
    <div class="email">maya@willowcraneyoga.com.au</div>
    <div class="address">
      <svg width="14" height="20" viewBox="0 0 14 20" aria-hidden="true">
        <path d="M7 0 C3 0 0 3 0 7 C0 12 7 20 7 20 C7 20 14 12 14 7 C14 3 11 0 7 0 Z" fill="var(--white)"/>
        <circle cx="7" cy="7" r="2.6" fill="var(--sky)"/>
      </svg>
      <span>The Chapel, 1420 Harbour Road Eastlake NSW 2099</span>
    </div>
  </footer>
</main>
</body>
</html>
```